Yacht Management in Miami & Ft Lauderdale (2019Q2)

I’m looking for a flyer to leave places for people to get information about my company and what services we offer.
We offer monthly management plans to ensure the vessel is ready to go at a moments notice. This can be as simple as washing once a week, or as involved as washing, waxing, detailing, provisioning, and crew services.
We also offer bespoke customizations; stereos, on board WiFi, and engineering.

Target Market(s)

Yacht and boat owners.

Font styles to use
Sans Serif

Colors
87d0c7
85cae6
85acd3
cedeed
cee9f5
cfeae6
0455a3

Requirements
Must have
• Must have simple attention grabbing, without being obnoxious.
• Prefer a 3in x 5in post card size. other size may be an option.
• Must be front and back.
Nice to have
• Languages: English, Spanish, Russian
• USA flag logo
Should not have
• Should not have a lot of text. Icons and photos are great.

```html
<!DOCTYPE html>
<html lang="en">
<head>
<meta charset="utf-8">
<title>Harbor Helm – Yacht Service Flyer</title>
<link rel="stylesheet" href="https://fonts.googleapis.com/css2?family=Roboto:wght@400;700;900&display=swap">
<style>
  :root {
    --red: #e8222a;
    --red-dark: #a3151b;
    --black: #111111;
    --white: #ffffff;
    --ink: #0d0d0d;
    --grey-text: #9a9a9a;
    --backdrop: #d6d6d6;
    --sea-deep: #123a78;
    --sea-mid: #2f66a8;
    --sea-foam: #c9d8ea;
  }
  * { box-sizing: border-box; margin: 0; padding: 0; }
  html, body { width: 1200px; height: 900px; overflow: hidden; }
  body {
    background: var(--backdrop);
    font-family: "Roboto", Arial, sans-serif;
    position: relative;
  }
  .flyer {
    position: absolute;
    left: 310px; top: 40px;
    width: 580px; height: 820px;
    background: var(--white);
    overflow: hidden;
    box-shadow: 0 6px 18px rgba(0,0,0,0.18);
  }
  .hero-photo {
    position: absolute; left: 0; top: 0;
    width: 580px; height: 320px;
    background: linear-gradient(160deg, var(--sea-deep) 0%, var(--sea-mid) 45%, var(--sea-foam) 70%, var(--sea-mid) 100%);
  }
  .shapes { position: absolute; left: 0; top: 0; }
  .crew-photo {
    position: absolute; left: 418px; top: 36px;
    width: 110px; height: 110px; border-radius: 50%;
    border: 4px solid var(--white);
    background: radial-gradient(circle at 40% 40%, #f2f2f2 0%, #9fb6cf 60%, #4c6f99 100%);
  }
  .tag {
    position: absolute; color: var(--white); font-weight: 700;
    text-transform: none; line-height: 1.05;
  }
  .tag-available { left: 22px; top: 196px; font-size: 19px; }
  .tag-crew {
    left: 362px; top: 168px; font-size: 16px; text-transform: uppercase;
    transform: rotate(-28deg); transform-origin: left top;
  }
  .icon-row { position: absolute; left: 60px; top: 236px; display: flex; gap: 26px; }
  .icon-row svg { width: 28px; height: 28px; display: block; }
  .services-copy {
    position: absolute; left: 30px; top: 282px; width: 262px;
    font-size: 18px; font-weight: 700; line-height: 1.18; color: var(--ink);
    hyphens: manual;
  }
  .brand {
    position: absolute; left: 330px; top: 248px; width: 220px;
    display: flex; align-items: center; justify-content: center; gap: 10px;
  }
  .brand-dot { width: 22px; height: 22px; border-radius: 50%; background: var(--ink); }
  .brand-name { font-size: 26px; font-weight: 900; color: var(--ink); }
  .headline {
    position: absolute; left: 310px; top: 330px; width: 260px;
    text-align: center; font-weight: 900; color: var(--ink); line-height: 1;
  }
  .headline-top { font-size: 32px; display: block; }
  .headline-yacht { font-size: 50px; color: var(--red); letter-spacing: 14px; display: block; margin: 6px 0 4px 14px; }
  .headline-bottom { font-size: 28px; display: block; }
  .consult {
    position: absolute; left: 190px; top: 580px; width: 370px;
    text-align: center; color: var(--white); font-weight: 700;
  }
  .consult-label { font-size: 17px; text-transform: uppercase; display: block; letter-spacing: 0.5px; }
  .consult-phone { font-size: 36px; display: block; line-height: 1.05; }
  .booking {
    position: absolute; left: 180px; top: 690px; width: 380px;
    text-align: center; color: var(--white);
  }
  .booking-title { font-size: 22px; font-weight: 700; text-transform: uppercase; display: block; }
  .booking-address { font-size: 14px; color: var(--grey-text); display: block; margin-top: 8px; }
  .booking-web { font-size: 14px; display: block; margin-top: 4px; }
</style>
</head>
<body>
  <main class="flyer">
    <div class="hero-photo" role="img" aria-label="Photo of a luxury motor yacht cruising at speed over deep blue water"></div>

    <svg class="shapes" width="580" height="820" viewBox="0 0 580 820" aria-hidden="true">
      <polygon points="0,310 220,222 580,222 580,560 0,560" fill="var(--white)"/>
      <polygon points="0,165 215,222 0,300" fill="var(--red)"/>
      <polygon points="300,222 580,70 580,222" fill="var(--red)"/>
      <polygon points="0,660 580,620 580,820 0,820" fill="var(--black)"/>
      <polygon points="0,648 580,608 580,618 0,658" fill="var(--red)"/>
      <polygon points="160,590 190,570 190,660 160,640" fill="var(--red-dark)"/>
      <polygon points="190,570 580,548 580,640 190,660" fill="var(--red)"/>
    </svg>

    <div class="crew-photo" role="img" aria-label="Round photo of a yacht deck with crew at work"></div>

    <p class="tag tag-available">Are<br>Available<br>24/7</p>
    <p class="tag tag-crew">Captaining &amp;<br>Crew</p>

    <div class="icon-row">
      <svg viewBox="0 0 28 28" role="img" aria-label="Stereo">
        <circle cx="14" cy="14" r="14" fill="var(--red)"/>
        <path d="M11 19.5V9l8-2v10" fill="none" stroke="var(--white)" stroke-width="2"/>
        <circle cx="9.5" cy="19.5" r="2.3" fill="var(--white)"/>
        <circle cx="17.5" cy="17.5" r="2.3" fill="var(--white)"/>
      </svg>
      <svg viewBox="0 0 28 28" role="img" aria-label="Detailing">
        <circle cx="14" cy="14" r="14" fill="var(--red)"/>
        <ellipse cx="14" cy="14" rx="8" ry="5" fill="none" stroke="var(--white)" stroke-width="2"/>
        <circle cx="14" cy="14" r="2.4" fill="var(--white)"/>
      </svg>
      <svg viewBox="0 0 28 28" role="img" aria-label="On board WiFi">
        <circle cx="14" cy="14" r="14" fill="var(--red)"/>
        <path d="M7 12a10 10 0 0 1 14 0M9.5 15a6 6 0 0 1 9 0" fill="none" stroke="var(--white)" stroke-width="2" stroke-linecap="round"/>
        <circle cx="14" cy="18.5" r="1.8" fill="var(--white)"/>
      </svg>
    </div>

    <p class="services-copy">We offer monthly man&shy;agement plans to ensure the vessel is ready to go at a moments notice. This can be as simple as washing once a week, or as involved as washing, waxing, detailing, provi&shy;sioning, and crew ser&shy;vices.<br>We also offer bespoke customizations; stereos, on board WiFi, and engi&shy;neering.</p>

    <div class="brand">
      <span class="brand-dot"></span>
      <span class="brand-name">Harbor Helm</span>
    </div>

    <h1 class="headline">
      <span class="headline-top">FAIR FRIENDLY</span>
      <span class="headline-yacht">YACHT</span>
      <span class="headline-bottom">SERVICE</span>
    </h1>

    <p class="consult">
      <span class="consult-label">Free Consultation</span>
      <span class="consult-phone">(555) 014-2280</span>
    </p>

    <p class="booking">
      <span class="booking-title">Book an Appointment</span>
      <span class="booking-address">480 Bayline Ave, #210 Coral Key, FL 33000</span>
      <span class="booking-web">www.harborhelm.co</span>
    </p>
  </main>
</body>
</html>
```